Eye Catching Business Card for Optometrist

We've recently refreshed our logo and now we need a fresh and bold look for our business cards. We provide progressive ways to improve people's vision and protect their eye health.

Use our new logo as guidance into the colors to use. As far as style goes, I love how bold and eye catching the card is for Lanternfly Studio. Feel free to use your creative judgement.

Tagline: "Sharply focused on your sight."

pertinent info to include:

Dr. Martin Sowerby
Optometrist

2857 Bramwell Ridge Blvd #217
Marlow Springs, MO 64190
(555) 382-7190

marty@brightlenshomeoptics.example
www.brightlenshomeoptics.example

```html
<!DOCTYPE html>
<html lang="en">
<head>
<meta charset="utf-8">
<title>Brightlens Home Optics – Business Card</title>
<link href="https://fonts.googleapis.com/css2?family=Source+Sans+3:wght@400;600;700&display=swap" rel="stylesheet">
<style>
  :root {
    --brown: #6a5646;
    --red: #c8273a;
    --beige: #d3b999;
    --white: #ffffff;
    --ink: #3a3029;
    --backdrop: #ece8e3;
    --card-w: 540px;
    --card-h: 309px;
  }
  * { box-sizing: border-box; margin: 0; padding: 0; }
  html, body { width: 1200px; height: 800px; overflow: hidden; }
  body {
    background: var(--backdrop);
    font-family: "Source Sans 3", Arial, sans-serif;
    color: var(--ink);
    display: flex;
    align-items: center;
    justify-content: center;
    gap: 40px;
  }
  .card {
    position: relative;
    width: var(--card-w);
    height: var(--card-h);
    background: var(--white);
    box-shadow: 0 6px 18px rgba(0,0,0,0.18);
    overflow: hidden;
  }

  /* Brand name set in place of the mark */
  .brand {
    display: flex;
    align-items: center;
    gap: 10px;
  }
  .brand-square {
    width: 22px;
    height: 22px;
    background: var(--red);
    flex: none;
  }
  .brand-name {
    font-weight: 700;
    color: var(--red);
    font-size: 24px;
    line-height: 1.05;
    text-transform: uppercase;
  }

  /* Front: name side */
  .card-front .person {
    position: absolute;
    top: 40px;
    left: 318px;
  }
  .person-name { font-size: 21px; font-weight: 400; }
  .person-title { font-size: 17px; font-weight: 400; margin-top: 2px; }
  .card-front .brand {
    position: absolute;
    left: 34px;
    top: 130px;
  }
  .card-front .brand-name { width: 170px; }
  .card-front .email {
    position: absolute;
    right: 26px;
    top: 196px;
    font-size: 14px;
  }
  .checker {
    position: absolute;
    left: 0; right: 0; bottom: 0;
    height: 76px;
    display: grid;
    grid-template-columns: repeat(10, 1fr);
    grid-template-rows: 1fr 1fr;
  }
  .checker span.brown { background: var(--brown); }
  .checker span.red { background: var(--red); }
  .checker span.beige { background: var(--beige); }

  /* Back: company side */
  .card-back .brand {
    position: absolute;
    top: 52px;
    left: 0; right: 0;
    justify-content: center;
  }
  .card-back .brand-name { font-size: 28px; }
  .tagline {
    position: absolute;
    top: 120px;
    left: 0; right: 0;
    text-align: center;
    font-size: 18px;
    font-weight: 600;
    color: var(--brown);
  }
  .contact-band {
    position: absolute;
    left: 0; right: 0; bottom: 0;
    height: 140px;
    background: var(--beige);
  }
  .band-stripe {
    position: absolute;
    top: 0; bottom: 0;
    width: 46px;
  }
  .band-stripe.brown { left: 0; background: var(--brown); }
  .band-stripe.red { left: 46px; background: var(--red); }
  .address {
    position: absolute;
    right: 22px;
    top: 16px;
    text-align: right;
    font-size: 14px;
    line-height: 1.3;
    color: var(--brown);
    font-style: normal;
  }
  .website {
    display: block;
    margin-top: 4px;
    font-size: 15px;
    color: var(--red);
    text-decoration: none;
  }
</style>
</head>
<body>

  <section class="card card-front" aria-label="Business card, front">
    <div class="person">
      <p class="person-name">Dr. Martin Sowerby</p>
      <p class="person-title">Optometrist</p>
    </div>
    <div class="brand">
      <span class="brand-square"></span>
      <span class="brand-name">Brightlens Home Optics</span>
    </div>
    <p class="email">marty@brightlenshomeoptics.example</p>
    <div class="checker" aria-hidden="true">
      <span></span><span></span><span></span><span></span>
      <span class="brown"></span><span class="red"></span><span class="beige"></span>
      <span class="brown"></span><span class="red"></span><span class="beige"></span>
      <span class="brown"></span><span class="red"></span><span class="beige"></span>
      <span class="brown"></span><span class="red"></span><span class="beige"></span>
      <span class="brown"></span><span class="red"></span><span class="beige"></span>
      <span class="brown"></span>
    </div>
  </section>

  <section class="card card-back" aria-label="Business card, back">
    <div class="brand">
      <span class="brand-square"></span>
      <span class="brand-name">Brightlens Home Optics</span>
    </div>
    <p class="tagline">Sharply focused on your sight.</p>
    <div class="contact-band">
      <span class="band-stripe brown"></span>
      <span class="band-stripe red"></span>
      <address class="address">
        2857 Bramwell Ridge Blvd #217<br>
        Marlow Springs, MO 64190<br>
        (555) 382-7190
        <a class="website" href="#">www.brightlenshomeoptics.example</a>
      </address>
    </div>
  </section>

</body>
</html>
```